Redesign of 3-4 page site for professional services firm

Our site is www.kestrelvaleadvisors.com. We currently have a simple page made with HostPlumo tools. But the tools are not able to generate the look and feel we desire. We need a home page similar to current that tells a little about our company, our experience and our team. We need a second page to show details of current and past transactions we have assisted our clients with. Currently this page reads like a word document but we would like for it to present in a cleaner fashion and liven it up with some images that link to the industry served. For example, a motorcycle outline in a circle for the powersports related transactions. We would like page to introduce each member of "Our Team" and highlight their experience with a photo of each person. If there is no photo available, we would like a placeholder to be their initials in a circle that can be updated later. We would also like a contact us section whether this is a different page or part of the home page.

Target Market(s)

Retirement minded business owners

Industry/Entity Type

Professional Services

Coding

Coded - Design and coding required

Requirements
Must have
• See project description. Must include a page or section for "Current Listings" and "Recently Completed Transactions" (can be same page)

```html
<!DOCTYPE html>
<html lang="en">
<head>
<meta charset="utf-8">
<title>Kestrel Vale Advisors</title>
<link href="https://fonts.googleapis.com/css2?family=Merriweather:wght@700;900&family=Poppins:wght@400;500;600&display=swap" rel="stylesheet">
<style>
:root{
  --green:#12b00e;
  --green-dark:#0d8f0a;
  --yellow:#d7cc1b;
  --gold:#d4b233;
  --red:#e3080f;
  --ink:#1b1b1b;
  --grey:#8c8c8c;
  --grey-bg:#e8e9ec;
  --black:#111;
  --white:#fff;
}
*{margin:0;padding:0;box-sizing:border-box}
html,body{width:1200px;height:5176px;overflow:hidden;background:var(--white)}
body{font-family:'Poppins',sans-serif;color:var(--ink)}
.page{position:relative;width:1200px;height:5176px;overflow:hidden}
.abs{position:absolute}
h1,h2,h3,.serif{font-family:'Merriweather',serif;font-weight:900}
.accent{color:var(--green)}
.btn{position:absolute;display:flex;align-items:center;justify-content:center;background:var(--red);color:var(--white);font-weight:600;font-size:15px;border-radius:22px;letter-spacing:.3px}
.section-title{font-size:46px;line-height:1.1;color:var(--ink);white-space:nowrap}
.body-grey{color:var(--grey);font-size:18px;line-height:23px}

/* nav */
.nav{left:52px;top:26px;width:1092px;height:74px;background:var(--white);border-radius:37px;box-shadow:0 2px 8px rgba(0,0,0,.08)}
.brand{position:absolute;left:48px;top:24px;font-weight:500;font-size:22px;color:var(--ink)}
.brand-dot{display:inline-block;width:14px;height:14px;background:var(--green);border-radius:50%;margin-right:8px;vertical-align:1px}
.nav-links{position:absolute;left:290px;top:29px;display:flex;gap:46px;font-size:13.5px;font-weight:500}
.nav-quote{right:34px;left:auto;top:18px;width:160px;height:40px;background:var(--yellow);color:var(--ink);font-size:14px}

/* hero */
.hero-title{left:58px;top:255px;font-size:50px;line-height:56px;color:#1a1a1a}
.hero-text{left:60px;top:440px;width:550px;font-size:13px;line-height:16px;color:#1f2a12}
.badge{position:absolute;background:var(--white);border-radius:12px;box-shadow:0 3px 10px rgba(0,0,0,.15);text-align:center}

/* team */
.team-card{position:absolute;top:2556px;width:296px;height:336px;border-radius:6px;overflow:hidden;background:linear-gradient(180deg,#f4f4f4 0%,#b9b9b9 45%,#3a3a3a 75%,#0d0d0d 100%)}
.team-card .name{position:absolute;left:32px;top:260px;font-family:'Merriweather',serif;font-weight:900;color:var(--white);font-size:19px}
.team-card .role{position:absolute;left:32px;top:288px;color:var(--yellow);font-size:18px}

/* listings */
.listing{position:absolute;top:3450px;width:330px}
.listing .photo{width:330px;height:214px;background:linear-gradient(180deg,#7a8a96 0%,#3d4147 45%,#1b1e2a 100%);position:relative;overflow:hidden}
.listing .ribbon{position:absolute;right:-44px;top:26px;width:180px;height:30px;background:var(--red);transform:rotate(45deg);color:var(--white);font-size:13px;font-weight:500;text-align:center;line-height:30px}
.listing h3{margin:28px 0 0 12px;font-size:19px;font-weight:900;white-space:nowrap}
.listing .loc{margin:4px 0 0 12px;color:var(--gold);font-size:15px;font-weight:500}
.listing p{margin:10px 0 0 12px;width:300px;font-size:10px;line-height:17px;color:#777}
.listing .btn{position:static;width:140px;height:32px;margin:20px 0 0 12px;font-size:14px}

/* reviews */
.review{position:absolute;top:4166px;width:304px;height:366px;border:3px solid #cfcfcf;text-align:center}
.review .avatar{width:94px;height:94px;border-radius:50%;margin:28px auto 0;background:radial-gradient(circle,#b58a6a,#5a4437)}
.review .who{margin-top:26px;font-family:'Merriweather',serif;font-weight:900;font-size:14px}
.review p{margin:10px auto 0;width:230px;color:var(--grey);font-size:18px;line-height:22px}
.review .stars{margin-top:16px;color:var(--yellow);font-size:22px;letter-spacing:3px}
.quote-mark{position:absolute;left:16px;top:12px}

/* footer */
.footer-head{position:absolute;top:4880px;font-family:'Merriweather',serif;font-weight:900;font-size:15px;color:var(--white)}
.footer-links{position:absolute;left:372px;top:4932px;display:flex;flex-direction:column;gap:21px;color:var(--white);font-size:15px}
.contact-row{position:absolute;left:570px;display:flex;gap:24px;color:var(--white);font-size:15px;line-height:25px}
.social{position:absolute;top:4988px;width:28px;height:28px;border-radius:50%;background:var(--green)}
</style>
</head>
<body>
<div class="page">

  <svg class="abs" style="left:0;top:0" width="1200" height="830" viewBox="0 0 1200 830">
    <defs>
      <linearGradient id="heroGrad" x1="0" y1="0" x2="1" y2="0.3">
        <stop offset="0" stop-color="#d6cb1d"/>
        <stop offset="0.45" stop-color="#7cc015"/>
        <stop offset="1" stop-color="#11b10e"/>
      </linearGradient>
    </defs>
    <path d="M0 0H1200V735C1020 700 870 700 640 760C420 815 200 805 0 730Z" fill="url(#heroGrad)"/>
    <path d="M0 730C200 805 420 815 640 760C870 700 1020 700 1200 735V748C1020 720 870 720 640 780C420 835 200 825 0 762Z" fill="var(--gold)"/>
  </svg>

  <nav class="abs nav">
    <div class="brand"><span class="brand-dot"></span>Kestrel Vale</div>
    <div class="nav-links"><span>HOME</span><span>ABOUT</span><span>BUSINESS LISTINGS</span><span>TEAM</span><span>REVIEWS</span></div>
    <div class="btn nav-quote">GET A QUOTE</div>
  </nav>

  <h1 class="abs hero-title">Strategically<br>Navigating<br>Business Exits</h1>
  <p class="abs hero-text">Lorem ipsum dolor sit amet, consectetuer adipiscing elit, sed diam nonummy nibh euismod tincidunt ut laoreet dolore magna aliquam erat volutpat. Ut wisi enim ad minim veniam, quis nostrud exerci tation ullamcorper suscipit lobortis nisl</p>
  <div class="btn" style="left:57px;top:538px;width:294px;height:42px">BOOK A FREE CONSULTATION</div>

  <svg class="abs" style="left:680px;top:185px" width="480" height="490" viewBox="0 0 480 490">
    <circle cx="245" cy="245" r="238" fill="none" stroke="#fff" stroke-width="2"/>
  </svg>
  <div class="abs" role="img" aria-label="Photo of a young woman sitting cross-legged with a laptop" style="left:720px;top:220px;width:360px;height:480px;border-radius:24px;background:linear-gradient(180deg,rgba(240,165,110,.85) 0%,rgba(240,165,110,.85) 50%,rgba(130,145,160,.85) 80%,rgba(200,204,208,.85) 100%)"></div>
  <div class="badge" style="left:668px;top:242px;width:106px;height:96px">
    <svg width="70" height="36" viewBox="0 0 70 36" style="margin-top:10px">
      <rect x="4" y="6" width="7" height="28" fill="#c8161b"/><rect x="14" y="14" width="7" height="20" fill="#c8161b"/>
      <rect x="24" y="20" width="7" height="14" fill="#d99a1a"/><rect x="34" y="16" width="7" height="18" fill="#d6c21b"/>
      <rect x="44" y="22" width="7" height="12" fill="#d6c21b"/><rect x="54" y="10" width="7" height="24" fill="#d6c21b"/>
    </svg>
    <div style="font-size:10px">Transactions</div>
    <div style="font-size:14px;font-weight:600">100+</div>
  </div>
  <div class="badge" style="left:1066px;top:386px;width:100px;height:94px">
    <div class="serif" style="font-size:9px;margin-top:14px;line-height:11px">SELL YOUR<br>BUSINESS</div>
    <svg width="80" height="36" viewBox="0 0 80 36">
      <path d="M4 28C20 26 34 22 46 16S66 6 74 4" fill="none" stroke="#c8161b" stroke-width="2"/>
      <line x1="4" y1="32" x2="76" y2="32" stroke="#d6c21b" stroke-width="2" stroke-dasharray="6 4"/>
    </svg>
  </div>

  <div class="abs" role="img" aria-label="Photo of a businessman signing a document" style="left:84px;top:972px;width:440px;height:400px;border-radius:38px;background:linear-gradient(160deg,#2d3340 0%,#4a5160 45%,#e6e7ea 75%,#f6f6f6 100%)"></div>
  <h2 class="abs section-title" style="left:598px;top:1016px">About <span class="accent">Kestrel Vale</span></h2>
  <p class="abs body-grey" style="left:598px;top:1092px;width:496px">Lorem ipsum dolor sit amet, consectetuer adipiscing elit, sed diam nonummy nibh euismod tincidunt ut laoreet dolore magna aliquam erat volutpat. Ut wisi enim ad minim veniam, quis nostrud exerci tation ullamcorper suscipit lobortis nisl ut aliquip ex ea commodo consequat. Duis</p>
  <div class="btn" style="left:598px;top:1266px;width:194px;height:42px">MORE ABOUT US</div>

  <h2 class="abs section-title" style="left:84px;top:1548px">Our <span class="accent">Experience</span></h2>
  <p class="abs body-grey" style="left:88px;top:1630px;width:596px">At Kestrel Vale Advisors, our mission is to empower entrepreneurs and business oWith decades of experience Kestrel Vale Advisors has proudly assisted numerous clients in successfully navigating the intricate journey of selling their businesses. Our team brings a wealth of knowledge and expertise acquired through years of working closely with entrepreneurs and business owners across diverse industries. We understand the unique challenges and complexities involved</p>
  <div class="btn" style="left:84px;top:1860px;width:216px;height:42px">GET STARTED NOW</div>
  <div class="abs" role="img" aria-label="Illustration of three rising arrows in red, olive and green" style="left:710px;top:1436px;width:406px;height:490px;border-radius:8px;background:linear-gradient(90deg,#e7b3b3 0%,#e2dcaa 50%,#b5dbb4 100%)"></div>

  <svg class="abs" style="left:0;top:2090px" width="1200" height="1120" viewBox="0 0 1200 1120">
    <path d="M0 82C120 40 230 10 420 60C640 120 820 150 1000 120C1090 105 1150 90 1200 84V1000C1120 990 1020 960 860 990C660 1030 520 1080 300 1090C170 1096 80 1080 0 1060Z" fill="var(--grey-bg)"/>
    <path d="M0 70C120 28 230 -2 420 48C640 108 820 138 1000 108C1090 93 1150 78 1200 72V88C1150 96 1090 110 1000 124C820 154 640 124 420 64C230 14 120 44 0 86Z" fill="var(--gold)"/>
    <path d="M0 1060C80 1080 170 1096 300 1090C520 1080 660 1030 860 990C1020 960 1120 990 1200 1000V1022C1120 1008 1020 980 860 1008C660 1048 520 1098 300 1108C170 1114 80 1098 0 1078Z" fill="var(--gold)"/>
  </svg>
  <h2 class="abs section-title" style="left:130px;top:2348px">Our <span class="accent">Team</span></h2>
  <p class="abs" style="left:130px;top:2416px;width:590px;font-size:13px;line-height:16px;color:#555">Together, our team of CPAs, attorneys, real estate brokers, and financial advisors work collaboratively to provide you with a holistic approach to business transactions. With our combined knowledge and experience, we strive to ensure a smooth and successful journey for our clients, delivering exceptional results and peace of mind.</p>
  <div class="btn" style="left:898px;top:2422px;width:166px;height:40px">VIEW ALL TEAM</div>
  <div class="team-card" style="left:124px" role="img" aria-label="Portrait photo of a team member"><div class="name">MARCUS DALTON</div><div class="role">CPA, JD</div></div>
  <div class="team-card" style="left:450px" role="img" aria-label="Portrait photo of a team member"><div class="name">OWEN HARTLEY</div><div class="role">Financial Advisor</div></div>
  <div class="team-card" style="left:776px" role="img" aria-label="Portrait photo of a team member"><div class="name">WALTER PRYCE</div><div class="role">Licensed Boker</div></div>

  <h2 class="abs section-title" style="left:0;width:1216px;text-align:center;top:3324px">Current <span class="accent">Listings</span></h2>
  <div class="listing" style="left:76px">
    <div class="photo" role="img" aria-label="Photo of motorcycles lined up in a dealership"><div class="ribbon">$1,100,000</div></div>
    <h3>Powersports Dealership</h3><div class="loc">NORTH TEXAS</div>
    <p>Well established multi-line dealership with strong net profit. Excellent staff in place. Dealership has a loyal customer base with further growth potential due to rapid community growth. Serious inquires with proof of funds only.</p>
    <div class="btn">VIEW MORE</div>
  </div>
  <div class="listing" style="left:432px">
    <div class="photo" role="img" aria-label="Photo of motorcycles lined up in a dealership"><div class="ribbon">SOLD</div></div>
    <h3>Sports and Entertainment Venue</h3><div class="loc">EAST TEXAS</div>
    <p>Well established multi-line dealership with strong net profit. Excellent staff in place. Dealership has a loyal customer base with further growth potential due to rapid community growth. Serious inquires with proof of funds only.</p>
    <div class="btn">VIEW MORE</div>
  </div>
  <div class="listing" style="left:786px">
    <div class="photo" role="img" aria-label="Photo of motorcycles lined up in a dealership"><div class="ribbon">$1,100,000</div></div>
    <h3>Powersports Dealership</h3><div class="loc">NORTH TEXAS</div>
    <p>Well established multi-line dealership with strong net profit. Excellent staff in place. Dealership has a loyal customer base with further growth potential due to rapid community growth. Serious inquires with proof of funds only.</p>
    <div class="btn">VIEW MORE</div>
  </div>

  <h2 class="abs section-title" style="left:0;width:1200px;text-align:center;top:4020px">Customer <span class="accent">Reviews</span></h2>
  <div class="review" style="left:102px">
    <svg class="quote-mark" width="34" height="30" viewBox="0 0 34 30"><path d="M2 4h12v12l-6 12H3l5-12H2Z M19 4h12v12l-6 12h-5l5-12h-6Z" fill="var(--green)"/></svg>
    <div class="avatar" role="img" aria-label="Customer photo"></div>
    <div class="who">DEAN CORWIN</div>
    <p>Lorem ipsum dolor sit amet, consectetuer adipiscing elit, sed diam nonummy nibh euismod tincidunt ut laoreet</p>
    <div class="stars">★★★★★</div>
  </div>
  <div class="review" style="left:452px">
    <svg class="quote-mark" width="34" height="30" viewBox="0 0 34 30"><path d="M2 4h12v12l-6 12H3l5-12H2Z M19 4h12v12l-6 12h-5l5-12h-6Z" fill="var(--green)"/></svg>
    <div class="avatar" role="img" aria-label="Customer photo"></div>
    <div class="who">TJ RAMSEY</div>
    <p>Lorem ipsum dolor sit amet, consectetuer adipiscing elit, sed diam nonummy nibh euismod tincidunt ut laoreet</p>
    <div class="stars">★★★★★</div>
  </div>
  <div class="review" style="left:804px">
    <svg class="quote-mark" width="34" height="30" viewBox="0 0 34 30"><path d="M2 4h12v12l-6 12H3l5-12H2Z M19 4h12v12l-6 12h-5l5-12h-6Z" fill="var(--green)"/></svg>
    <div class="avatar" role="img" aria-label="Customer photo"></div>
    <div class="who">NADIA R QUINN</div>
    <p>Lorem ipsum dolor sit amet, consectetuer adipiscing elit, sed diam nonummy nibh euismod tincidunt ut laoreet</p>
    <div class="stars">★★★★★</div>
  </div>

  <svg class="abs" style="left:0;top:4690px" width="1200" height="486" viewBox="0 0 1200 486">
    <path d="M0 60C140 100 300 110 520 80C760 46 940 20 1200 70V486H0Z" fill="var(--black)"/>
    <path d="M0 44C140 84 300 94 520 64C760 30 940 4 1200 54V70C940 20 760 46 520 80C300 110 140 100 0 60Z" fill="var(--gold)"/>
  </svg>
  <div class="abs" style="left:50px;top:4918px;font-size:24px;font-weight:500;color:var(--white)"><span class="brand-dot"></span>Kestrel Vale</div>
  <div class="social" style="left:70px"></div>
  <div class="social" style="left:116px"></div>
  <div class="social" style="left:162px"></div>

  <div class="footer-head" style="left:358px">QUICK LINKS</div>
  <div class="footer-links"><span>HOME</span><span>TEAM</span><span>LISTINGS</span><span>ABOUT</span><span>CONTACT</span></div>

  <div class="footer-head" style="left:570px">CONTACT NFO</div>
  <div class="contact-row" style="top:4926px">
    <svg width="22" height="22" viewBox="0 0 24 24"><path d="M6.6 10.8a15 15 0 0 0 6.6 6.6l2.2-2.2c.3-.3.7-.4 1-.2 1.1.4 2.3.6 3.6.6.6 0 1 .4 1 1V20c0 .6-.4 1-1 1A17 17 0 0 1 3 4c0-.6.4-1 1-1h3.5c.6 0 1 .4 1 1 0 1.3.2 2.5.6 3.6.1.3 0 .7-.2 1Z" fill="var(--yellow)"/></svg>
    <span>(555) 018 274</span>
  </div>
  <div class="contact-row" style="top:4974px">
    <svg width="22" height="22" viewBox="0 0 24 24"><rect x="2" y="5" width="20" height="14" rx="1" fill="var(--yellow)"/><path d="M2 6l10 7 10-7" fill="none" stroke="#111" stroke-width="1.5"/></svg>
    <span>hello@kestrelvale.com</span>
  </div>
  <div class="contact-row" style="top:5020px">
    <svg width="22" height="24" viewBox="0 0 24 24"><path d="M12 2a7 7 0 0 0-7 7c0 5 7 13 7 13s7-8 7-13a7 7 0 0 0-7-7Zm0 9.5A2.5 2.5 0 1 1 12 6.5a2.5 2.5 0 0 1 0 5Z" fill="var(--yellow)"/></svg>
    <span>402 Birchline Road, Ashford,<br>Oklahoma<br>74000, United States</span>
  </div>

  <div class="footer-head" style="left:930px">STAY UP-TO-DATE</div>
  <div class="abs" style="left:925px;top:4944px;width:202px;height:36px;border-radius:18px;background:#3a3a3a;color:#bbb;font-size:13px;display:flex;align-items:center;justify-content:center">EMAIL ADDRESS</div>
  <div class="btn" style="left:925px;top:4992px;width:202px;height:36px;font-size:13px">SUBSCRIBE NOW</div>

  <div class="abs" style="left:0;width:1216px;top:5146px;text-align:center;color:var(--white);font-size:12px">Copyright © 2023 Kestrel Vale Advisors - All Rights Reserved</div>
</div>
</body>
</html>
```